Custom Cabinet Shop Needs a website design

Hi,
We need a website for a Custom Cabinet Shop and Cabinet parts manufacturing business.
The business has two sides to it. One side provides custom Kitchens, vanities, entertainment units, offices and what not to homeowners and contractors.
The 2nd side of the business provides built to order cabinet boxes and other parts required to put together a project to other cabinet shops, small contractors looking to install there own cabinets.
Website will need a Gallery to display work.
Color scheme to go well with logo.
current website is www.brindlewoodcustomcabinets.com
being changed to www.brindlewood.ca
Logo Included in attached files.
Tagline "Millwork with Flare"
Mission Statement "Our passion is to deliver inspired cabinetry solutions to suit all your needs, supported by our phenomenal star class customer service"
The website should convey quality and professionalism.
Thank you.
Homeowners/ Contractors
Entertainment
Coded - Design and coding required
1 page

```html
<!DOCTYPE html>
<html lang="en">
<head>
<meta charset="utf-8">
<title>Brindlewood Custom Cabinets</title>
<link href="https://fonts.googleapis.com/css2?family=Open+Sans:wght@300;400;600;700&display=swap" rel="stylesheet">
<style>
  :root {
    --orange: #f26a2e;
    --orange-soft: #f58a5a;
    --hero-dark: #1d1f24;
    --hero-mid: #3b3530;
    --hero-warm: #6a4a30;
    --white: #ffffff;
    --ink: #333333;
    --page: #ffffff;
    --dot: #cfcfcf;
  }
  html, body {
    margin: 0;
    width: 1200px;
    height: 857px;
    overflow: hidden;
    background: var(--page);
    font-family: "Open Sans", Arial, sans-serif;
  }
  .site { width: 1200px; height: 857px; position: relative; overflow: hidden; }

  .top-rule { height: 4px; background: var(--orange); }

  .hero {
    position: relative;
    height: 690px;
    background:
      radial-gradient(ellipse at 30% 75%, var(--hero-warm) 0%, rgba(106,74,48,0) 55%),
      linear-gradient(180deg, #4a4642 0%, var(--hero-mid) 45%, var(--hero-dark) 100%);
  }

  .header {
    position: absolute; top: 0; left: 0; right: 0;
    height: 100px;
    display: flex; align-items: center; justify-content: space-between;
    padding: 0 60px 0 95px;
  }
  .brand {
    display: flex; align-items: center; gap: 12px;
    color: var(--white); font-weight: 700; font-size: 26px; letter-spacing: 1px;
  }
  .brand-mark { width: 16px; height: 16px; background: var(--white); }
  .nav { display: flex; gap: 34px; }
  .nav a { color: var(--white); text-decoration: none; font-size: 15px; font-weight: 400; }
  .nav a.current { font-weight: 600; }

  .search-btn {
    position: absolute; top: 118px; right: 60px;
    width: 40px; height: 40px; background: var(--orange-soft);
    display: flex; align-items: center; justify-content: center;
  }

  .hero-copy {
    position: absolute; right: 90px; top: 300px;
    text-align: right; color: var(--white);
  }
  .hero-copy h1 {
    margin: 0; font-weight: 300; font-size: 40px; line-height: 52px; text-transform: uppercase;
  }
  .btn-learn {
    display: inline-block; margin-top: 22px;
    background: var(--orange); color: var(--white);
    font-size: 14px; padding: 10px 20px; text-transform: uppercase; text-decoration: none;
  }

  .slide-arrow {
    position: absolute; top: 400px; width: 36px; height: 44px; background: var(--orange);
    display: flex; align-items: center; justify-content: center;
  }
  .slide-arrow.prev { left: 0; }
  .slide-arrow.next { right: 0; }

  .slide-dots { position: absolute; bottom: 18px; left: 50%; transform: translateX(-50%); display: flex; gap: 8px; }
  .slide-dots span { width: 9px; height: 9px; border-radius: 50%; background: var(--dot); }
  .slide-dots span.active { background: var(--orange); }

  .welcome {
    height: 92px; background: var(--orange); color: var(--white);
    text-align: center; display: flex; flex-direction: column; justify-content: center;
  }
  .welcome small { font-size: 14px; text-transform: uppercase; letter-spacing: 1px; }
  .welcome strong { font-size: 24px; font-weight: 600; }

  .about { padding: 28px 160px; display: flex; gap: 40px; }
  .about-photo { width: 380px; height: 150px; background: linear-gradient(135deg, #5a3a2a, #2c2c30); }
  .about h2 { margin: 0; font-size: 16px; font-weight: 700; color: var(--ink); }
</style>
</head>
<body>
<div class="site">
  <div class="hero" role="img" aria-label="Photo of a dark basement bar with a live-edge wood counter, stools and pendant lights">
    <div class="top-rule"></div>
    <header class="header">
      <div class="brand"><span class="brand-mark"></span>BRINDLEWOOD</div>
      <nav class="nav">
        <a class="current" href="#">Home</a>
        <a href="#">Gallery</a>
        <a href="#">Services</a>
        <a href="#">Warranty</a>
        <a href="#">Contact</a>
      </nav>
    </header>
    <div class="search-btn">
      <svg width="20" height="20" viewBox="0 0 20 20"><circle cx="8" cy="8" r="6" fill="none" stroke="#fff" stroke-width="2"/><line x1="12.5" y1="12.5" x2="18" y2="18" stroke="#fff" stroke-width="2.5"/></svg>
    </div>
    <div class="slide-arrow prev">
      <svg width="12" height="16" viewBox="0 0 12 16"><polyline points="9,2 3,8 9,14" fill="none" stroke="#fff" stroke-width="2"/></svg>
    </div>
    <div class="slide-arrow next">
      <svg width="12" height="16" viewBox="0 0 12 16"><polyline points="3,2 9,8 3,14" fill="none" stroke="#fff" stroke-width="2"/></svg>
    </div>
    <div class="hero-copy">
      <h1>Bringing style<br>and comfort for<br>customer satisfaction</h1>
      <a class="btn-learn" href="#">Learn more</a>
    </div>
    <div class="slide-dots"><span class="active"></span><span></span><span></span></div>
  </div>
  <section class="welcome">
    <small>Welcome to</small>
    <strong>Brindlewood Custom Cabinets</strong>
  </section>
  <section class="about">
    <div class="about-photo" role="img" aria-label="Photo of a finished kitchen island with cabinetry"></div>
    <h2>ABOUT US</h2>
  </section>
</div>
</body>
</html>
```